Verpackungen für kleine Imkerei
Zielgruppe
Wir sind eine kleine Imkerei aus dem Aargau (Schweiz) und stellen zusammen mit unseren glücklichen Bienen feinsten Honig her. Gerne möchten wir unseren visuelle Kommunikation nach aussen mit Hilfe eines neuen Etiketts verbessern.
Aufgabenstellung
Das Etikett muss rechteckig sein und wir auf einem runden Glas aufgeklebt. Die Maximalgrösse ist 210x45mm (beim 500g Glas) und entsprechend kleiner bei kleineren Einheiten. Wir möchten ein Grunddesign, welches adaptierbar ist auf die weiteren Sorten. (Waldhonig, Blütenhonig, cremiger Blütenhonig, Zürcher Stadthonig, Badener Stadthonig, Lenzburger Stadthonig). Barcode muss keinen eingefügt werden, nur die gesetzlichen Daten müssen auf dem Etiektt stehen. Weitere Wünsche und Anmerkungen befinden sich im pdf.
Sollten Dateien oder Bilder nachgereicht werden, bitte melden!

```html
<!DOCTYPE html>
<html lang="de">
<head>
<meta charset="utf-8">
<title>Summwiese – Etikett Waldhonig</title>
<link href="https://fonts.googleapis.com/css2?family=Roboto+Condensed:wght@400;700&display=swap" rel="stylesheet">
<style>
  :root {
    --page-bg: #ececec;
    --label-bg: #ffffff;
    --leaf-green: #6f9e2c;
    --band-green: #8dbb45;
    --wash-green: rgba(190, 219, 130, 0.75);
    --wash-soft: rgba(215, 233, 176, 0.7);
    --tree-green: rgba(170, 206, 110, 0.55);
    --ink: #1d1d1d;
    --bee-yellow: #e9b632;
  }
  html, body {
    margin: 0;
    width: 1200px;
    height: 800px;
    overflow: hidden;
    background: var(--page-bg);
    font-family: "Roboto Condensed", "Arial Narrow", sans-serif;
  }
  .label {
    position: absolute;
    left: 40px;
    top: 281px;
    width: 1120px;
    height: 238px;
    background: var(--label-bg);
    box-shadow: 0 2px 8px rgba(0,0,0,.12);
    overflow: hidden;
    color: var(--ink);
  }
  .wash {
    position: absolute;
    border-radius: 50%;
  }
  .wash--left   { left: 120px; top: -40px; width: 320px; height: 220px; background: radial-gradient(closest-side, var(--wash-green), rgba(255,255,255,0)); }
  .wash--center { left: 400px; top: 60px;  width: 360px; height: 220px; background: radial-gradient(closest-side, var(--wash-green), rgba(255,255,255,0)); }
  .wash--right  { left: 780px; top: -40px; width: 360px; height: 200px; background: radial-gradient(closest-side, var(--wash-green), rgba(255,255,255,0)); }
  .wash--bottom-left  { left: -80px; top: 130px; width: 480px; height: 200px; background: radial-gradient(closest-side, var(--wash-soft), rgba(255,255,255,0)); }
  .wash--bottom-right { left: 760px; top: 130px; width: 480px; height: 200px; background: radial-gradient(closest-side, var(--wash-soft), rgba(255,255,255,0)); }
  .forest {
    position: absolute;
    left: 260px;
    top: 80px;
    width: 700px;
    height: 220px;
    border-radius: 50%;
    background: radial-gradient(closest-side, var(--tree-green), rgba(255,255,255,0));
  }
  .band {
    position: absolute;
    left: 0; right: 0; bottom: 0;
    height: 18px;
    background: var(--band-green);
  }
  .info { position: absolute; top: 42px; font-size: 16.5px; line-height: 20px; }
  .info p { margin: 0 0 6px; }
  .info .key { color: var(--leaf-green); }
  .info--legal { left: 23px; }
  .info--contact { right: 23px; text-align: right; }
  .brand {
    position: absolute;
    left: 0; right: 0;
    top: 50px;
    text-align: center;
    font-size: 66px;
    line-height: 80px;
    font-weight: 700;
    letter-spacing: 1px;
    color: var(--ink);
  }
  .variety {
    position: absolute;
    left: 0; right: 0;
    top: 158px;
    text-align: center;
    font-size: 28px;
    line-height: 36px;
    font-weight: 700;
    letter-spacing: 1px;
    color: var(--leaf-green);
  }
  .bee {
    position: absolute;
    width: 22px; height: 17px;
    border-radius: 50%;
    background: var(--bee-yellow);
  }
</style>
</head>
<body>
  <section class="label">
    <div class="wash wash--bottom-left"></div>
    <div class="wash wash--bottom-right"></div>
    <div class="wash wash--left"></div>
    <div class="wash wash--center"></div>
    <div class="wash wash--right"></div>
    <div class="forest" role="img" aria-label="Gezeichnete Tannenwald-Silhouette in Hellgrün"></div>

    <div class="bee" style="left:232px;top:82px" role="img" aria-label="Kleine gezeichnete Biene"></div>
    <div class="bee" style="left:160px;top:150px" role="img" aria-label="Kleine gezeichnete Biene"></div>
    <div class="bee" style="left:495px;top:24px" role="img" aria-label="Kleine gezeichnete Biene"></div>
    <div class="bee" style="left:700px;top:20px" role="img" aria-label="Kleine gezeichnete Biene"></div>
    <div class="bee" style="left:460px;top:124px" role="img" aria-label="Kleine gezeichnete Biene"></div>
    <div class="bee" style="left:1000px;top:20px" role="img" aria-label="Kleine gezeichnete Biene"></div>
    <div class="bee" style="left:955px;top:128px" role="img" aria-label="Kleine gezeichnete Biene"></div>

    <div class="info info--legal">
      <p><span class="key">Schweizer Blütenhonig</span><br>Honig gut verschlossen,<br>Kühl (Bei max. 15°),<br>Dunkel und Trocken lagern</p>
      <p><span class="key">Mindestens Haltbar bis</span><br>August 2022</p>
      <p><span class="key">Warenlos Nr.</span> 01092018</p>
      <p><span class="key">Nettogewicht</span> 500g</p>
    </div>

    <div class="brand">Summwiese</div>
    <div class="variety">•WALDHONIG•</div>

    <div class="info info--contact">
      <p><span class="key">Adresse</span><br>Ursula und Stephan Karrigo<br>Lindenhofweg 14<br>5600 Ammerswil</p>
      <p><span class="key">Web</span><br>www.summwiese.ch</p>
      <p><span class="key">Mail</span><br>info@summwiese.ch</p>
    </div>

    <div class="band"></div>
  </section>
</body>
</html>
```